Publisher needs a book cover design for Workflow Insight Methods book

We need a book cover (front, back, spine) for the 3rd edition of a book entitled 'Workflow Insight Methods' and subtitled 'covering Structure, Design, Oversight and Growth Stages'. The author is Malcolm Feverill. The publisher is Halvenmoor Press. The finished size of the paperback version will be the industry standard 9" x 6". There will be paperback, hardback, and Kindle versions. The final number of pages is expected to be in the region 300-350 pages. Text for the back cover is not yet available, but at the bottom of the back cover should be publisher logo on the left and space for the ISBN bar code on the right.<br/>The design should be original and not include any stock images that have been created by someone else or may require obtaining a copyright licence to use. Symbols in common use and not copyrighted are probably ok.<br/>There are no required images, photographs or symbols except the publisher logo at the left bottom of the back cover and lower spine. S[ine lettering should be UK/US style with the top of the writing nearest the front cover. The designer is free to be creative using appropriate diagrams, symbols or abstract designs. Rectangular and circular variants of the publisher logo are attached.<br/>I just want to assure designers that when evaluating designs from my perspective, I take absolutely no notice whatsoever of a designer's Artisan Pool ranking or status; I am completely output driven, so what matters to me is the design, not the ranking or status of the designer. In a similar way, I do not evaluate designs as 'good' or 'bad' - the winning design will be chosen after review by a design panel.
Updates

More time is needed to check the use of stock images by designers. Some have been used by desitgners but not yet disclosed.

Target Market(s)

Practitioners and academics concerned with Workflow Insight Methods, Business Process Management, Business Process Architecture, Enterprise Architecture, Information Architecture, Process modelling, data modelling

Font styles to use
Serif
Sans Serif

Colors

Designer to choose colors to be used in the design.

Requirements
Must have
• Title, author, edition, subtitle, publisher logo.
Nice to have
• Originality, innovation
Should not have
• Stock images or anything else requiring additional copyright discussions and negotiations.

```html
<!DOCTYPE html>
<html lang="en">
<head>
<meta charset="utf-8">
<title>Workflow Insight Methods – Cover Layout</title>
<link rel="stylesheet" href="https://fonts.googleapis.com/css2?family=Archivo+Black&family=Fira+Sans:wght@300;400;800&display=swap">
<style>
  :root {
    --ink: #000000;
    --paper: #ffffff;
    --accent-red: #ff1a1a;
    --guide: #666666;
    --body-grey: #6d6d6d;
    --ghost-grey: #9a9a9a;
    --ghost-light: #c4c4c4;
    --frame: #444444;
  }
  * { box-sizing: border-box; margin: 0; padding: 0; }
  html, body { width: 1200px; height: 849px; overflow: hidden; background: var(--paper); }
  .sheet {
    position: relative; width: 1200px; height: 849px;
    border: 1px solid #bdbdbd; background: var(--paper);
    font-family: "Fira Sans", sans-serif; overflow: hidden;
  }
  .panel { position: absolute; top: 98px; height: 652px; border: 1px solid var(--frame); background: var(--paper); overflow: hidden; }
  .panel--back { left: 117px; width: 435px; }
  .panel--spine { left: 556px; width: 55px; }
  .panel--front { left: 615px; width: 435px; }

  /* guides */
  .guide-label { position: absolute; font-size: 10.5px; color: var(--guide); font-weight: 400; }
  .guide-rule { position: absolute; background: var(--guide); }

  /* back cover */
  .back-heading { position: absolute; left: 45px; font-family: "Fira Sans", sans-serif; font-weight: 800; font-size: 10px; color: #222; }
  .back-copy { position: absolute; font-weight: 300; font-size: 8.6px; line-height: 10.35px; color: var(--body-grey); white-space: nowrap; }
  .back-art {
    position: absolute; left: 224px; top: 276px; width: 165px; height: 272px;
    border: 1px solid var(--ink); border-radius: 8px;
    background: linear-gradient(180deg, #ffffff 0%, #ececec 55%, #ffffff 100%);
  }
  .isbn-box {
    position: absolute; left: 224px; top: 560px; width: 166px; height: 64px;
    border: 1px solid var(--ink); border-radius: 8px;
    display: flex; align-items: center; justify-content: center;
    font-size: 21px; color: #8a8a8a; font-weight: 400;
  }
  .publisher-mark { position: absolute; left: 42px; top: 575px; display: flex; align-items: center; gap: 6px; }
  .publisher-mark__dot { width: 36px; height: 36px; border-radius: 50%; background: var(--ink); }
  .publisher-mark__name { font-family: "Fira Sans", sans-serif; font-weight: 400; font-size: 14px; letter-spacing: 0.4px; color: var(--ink); line-height: 1; white-space: nowrap; }

  /* spine */
  .spine-text { position: absolute; left: 0; width: 55px; writing-mode: vertical-rl; display: flex; align-items: center; color: var(--ink); white-space: nowrap; }
  .spine-title { top: 17px; height: 232px; font-family: "Archivo Black", sans-serif; font-size: 12.5px; }
  .spine-author { top: 264px; font-family: "Archivo Black", sans-serif; font-size: 12px; }
  .spine-edition { top: 460px; font-family: "Fira Sans", sans-serif; font-weight: 800; font-size: 9px; }
  .spine-mark { position: absolute; left: 6px; top: 568px; width: 42px; text-align: center; }
  .spine-mark__dot { width: 22px; height: 22px; border-radius: 50%; background: var(--ink); margin: 0 auto 3px; }
  .spine-mark__name { font-size: 4.6px; font-weight: 400; letter-spacing: 0.2px; color: var(--ink); }

  /* front cover */
  .front-art {
    position: absolute; left: 200px; top: 150px; width: 190px; height: 380px;
    background: linear-gradient(160deg, rgba(240,240,240,0.6) 0%, rgba(215,215,215,0.55) 50%, rgba(245,245,245,0.4) 100%);
  }
  .title-block { position: absolute; left: 36px; top: 0; width: 212px; height: 314px; background: var(--ink); }
  .title-main { position: absolute; left: 5px; top: 5px; font-family: "Archivo Black", sans-serif; font-size: 32px; line-height: 40px; color: var(--paper); white-space: nowrap; }
  .subtitle { position: absolute; left: 10px; top: 135px; font-family: "Archivo Black", sans-serif; font-size: 15.5px; line-height: 23.3px; color: var(--accent-red); white-space: nowrap; }
  .subtitle__lead { letter-spacing: 5px; }
  .edition { position: absolute; left: 11px; top: 296px; font-family: "Fira Sans", sans-serif; font-weight: 800; font-size: 10.5px; color: var(--paper); }
  .ghost-word { position: absolute; left: 36px; font-family: "Archivo Black", sans-serif; white-space: nowrap; line-height: 1; }
  .ghost-word--structure { top: 312px; font-size: 30px; color: var(--ghost-grey); }
  .ghost-word--design { top: 460px; font-size: 34px; color: var(--ghost-grey); }
  .ghost-word--oversight { top: 490px; font-size: 34px; color: #8c8c8c; }
  .ghost-word--growth { top: 516px; font-size: 52px; color: var(--ghost-light); }
  .ghost-figure { position: absolute; left: 36px; top: 345px; font-family: "Archivo Black", sans-serif; font-size: 60px; line-height: 56px; color: #dadada; }
  .author-block { position: absolute; left: 36px; top: 567px; width: 213px; height: 85px; background: var(--ink); }
  .author-name { position: absolute; left: 12px; top: 13px; font-family: "Archivo Black", sans-serif; font-size: 17px; color: var(--paper); white-space: nowrap; }
  .growth-arrow { position: absolute; left: 0; top: 0; pointer-events: none; }
</style>
</head>
<body>
<div class="sheet">

  <span class="guide-label" style="left:818px; top:34px;">6 inch</span>
  <div class="guide-rule" style="left:615px; top:54px; width:435px; height:1px;"></div>
  <div class="guide-rule" style="left:615px; top:50px; width:1px; height:9px;"></div>
  <div class="guide-rule" style="left:1049px; top:50px; width:1px; height:9px;"></div>
  <div class="guide-rule" style="left:1098px; top:98px; width:1px; height:652px;"></div>
  <div class="guide-rule" style="left:1094px; top:98px; width:9px; height:1px;"></div>
  <div class="guide-rule" style="left:1094px; top:750px; width:9px; height:1px;"></div>
  <span class="guide-label" style="left:1108px; top:417px;">9 inch</span>
  <span class="guide-label" style="left:116px; top:766px;">Back</span>
  <span class="guide-label" style="left:569px; top:771px;">Spine</span>
  <span class="guide-label" style="left:1024px; top:764px;">Front</span>

  <section class="panel panel--back">
    <h2 class="back-heading" style="top:50px;">About This Book</h2>
    <p class="back-copy" style="left:44px; top:67px;">Introduction will be replaced by original text<br>Introduction will be replaced by original text<br>Introduction will be replaced by original text<br>Introduction will be replaced by original text<br>Introduction will be replaced by original text<br>Introduction will be replaced by original text<br>Introduction will be replaced by original text</p>
    <p class="back-copy" style="left:223px; top:67px;">Introduction will be replaced by original text<br>Introduction will be replaced by original text<br>Introduction will be replaced by original text<br>Introduction will be replaced by original text<br>Introduction will be replaced by original text<br>Introduction will be replaced by original text<br>Introduction will be replaced by original text</p>
    <p class="back-copy" style="left:44px; top:153px;">Introduction will be replaced by original text<br>Introduction will be replaced by original text<br>Introduction will be replaced by original text<br>Introduction will be replaced by original text<br>Introduction will be replaced by original text<br>Introduction will be replaced by original text<br>Introduction will be replaced by original text<br>Introduction will be replaced by original text<br>Introduction will be replaced by original text<br>Introduction will be replaced by original text</p>
    <p class="back-copy" style="left:223px; top:153px;">Introduction will be replaced by original text<br>Introduction will be replaced by original text<br>Introduction will be replaced by original text<br>Introduction will be replaced by original text<br>Introduction will be replaced by original text<br>Introduction will be replaced by original text<br>Introduction will be replaced by original text<br>Introduction will be replaced by original text<br>Introduction will be replaced by original text<br>Introduction will be replaced by original text</p>

    <h2 class="back-heading" style="top:272px;">About The AUthor</h2>
    <p class="back-copy" style="left:44px; top:288px;">Introduction will be replaced by original text<br>Introduction will be replaced by original text<br>Introduction will be replaced by original text<br>Introduction will be replaced by original text<br>Introduction will be replaced by original text<br>Introduction will be replaced by original text<br>Introduction will be replaced by original text<br>Introduction will be replaced by original text<br>Introduction will be replaced by original text<br>Introduction will be replaced by original text<br>Introduction will be replaced by original text<br>Introduction will be replaced by original text</p>
    <p class="back-copy" style="left:44px; top:435px;">Introduction will be replaced by original text<br>Introduction will be replaced by original text<br>Introduction will be replaced by original text<br>Introduction will be replaced by original text<br>Introduction will be replaced by original text<br>Introduction will be replaced by original text<br>Introduction will be replaced by original text<br>Introduction will be replaced by original text<br>Introduction will be replaced by original text<br>Introduction will be replaced by original text<br>Introduction will be replaced by original text</p>

    <div class="back-art" role="img" aria-label="Pen sketch of a hillside cluster of stacked houses with a bird perched on a line"></div>
    <div class="isbn-box">ISBN</div>

    <div class="publisher-mark">
      <span class="publisher-mark__dot"></span>
      <span class="publisher-mark__name">HALVENMOOR PRESS</span>
    </div>
  </section>

  <section class="panel panel--spine">
    <div class="spine-text spine-title">WORKFLOW INSIGHT METHODS</div>
    <div class="spine-text spine-author">Malcolm Feverill.</div>
    <div class="spine-text spine-edition">3rd edition</div>
    <div class="spine-mark">
      <div class="spine-mark__dot"></div>
      <div class="spine-mark__name">HALVENMOOR PRESS</div>
    </div>
  </section>

  <section class="panel panel--front">
    <div class="front-art" role="img" aria-label="Pen sketch of a tall hillside town of stacked buildings, towers, stairs and trees"></div>

    <div class="title-block">
      <h1 class="title-main">WORKFLOW<br>INSIGHT<br>METHODS</h1>
      <p class="subtitle"><span class="subtitle__lead">COVERING</span><br>STRUCTURE<br>DESIGN<br>OVERSIGHT<br>&amp; GROWTH STAGES</p>
      <p class="edition">3rd edition</p>
    </div>

    <div class="ghost-figure">3.5<br>12</div>
    <div class="ghost-word ghost-word--structure">STRUCTURE</div>
    <div class="ghost-word ghost-word--design">DESIGN STAGES</div>
    <div class="ghost-word ghost-word--oversight">OVERSIGHT</div>
    <div class="ghost-word ghost-word--growth">GROWTH</div>

    <div class="author-block">
      <p class="author-name">Malcolm Feverill.</p>
    </div>
  </section>

  <svg class="growth-arrow" width="1200" height="849" viewBox="0 0 1200 849" aria-hidden="true">
    <path d="M281 519 C 430 515, 560 500, 640 462 C 760 410, 880 350, 998 272" fill="none" stroke="#5a5a5a" stroke-width="1.6"/>
    <path d="M281 519 C 390 515, 470 510, 560 494 C 600 486, 620 478, 640 470" fill="none" stroke="#1a1a1a" stroke-width="4" stroke-linecap="round"/>
    <path d="M988 272 L 999 271 L 994 281" fill="none" stroke="#5a5a5a" stroke-width="1.2"/>
  </svg>
</div>
</body>
</html>
```